Brack and Loam LLC | Land Clearing, Landscaping & Dump Trailer Services

Project Description: Brack and Loam LLC Website Design
The website will be published using squarespace
Objective:
Design a visually compelling and conversion-driven website for Brack and Loam LLC, a land solutions business based in Pickens County, Georgia. The site will highlight the company’s professionalism, locally rooted service, and commitment to quality in land clearing, grading, and dump trailer services.
Pages & Features to Include:
1. Landing Page (Homepage)
- Clear tagline: Shaping Ground with Care and Grit
- Call-to-Action (CTA) buttons: “Get a Free Quote” and “View Services”
- Service highlights with icons or photos (e.g., grading, mulching, hauling)
- Customer testimonials
- Embedded contact form
- Google Maps integration showing service area
2. Services + Pricing Page
- Organized list of services under 3 categories:
- **Land Clearing & Grading**
- Forestry Mulching
- Gravel Driveway Repair
- Minimum Job Fee:
- Dump Trailer Services
- Trailer Rental (Daily):
- Junk Removal (Full Load)
- Material Delivery: $ + mileage
- Specialty Jobs
- Stump removal, light demolition
- Each service section includes short descriptions and photos
- Optional quote form at the bottom with “Request a Quote” CTA
Design Style:
- Clean, professional design using clean tones
- Fonts that balance industrial strength and local charm
- Mobile-optimized with fast loading speeds and easy navigation
- SEO-optimized for terms like *land clearing Pickens County*, *grading services North Georgia*, and *dump trailer rental Jasper GA*, etc...

```html
<!DOCTYPE html>
<html lang="en">
<head>
<meta charset="utf-8">
<title>Brack and Loam LLC | Land Clearing Pickens County</title>
<link href="https://fonts.googleapis.com/css2?family=Poppins:wght@400;500;600;700&family=Open+Sans:wght@400;600&display=swap" rel="stylesheet">
<style>
:root{
  --green:#3f8a2e;
  --green-dark:#2f6f22;
  --ink:#1e1e1e;
  --text:#444;
  --muted:#777;
  --mint:#eaf6e4;
  --mint-2:#f4faf1;
  --white:#fff;
  --line:#d9d9d9;
}
*{box-sizing:border-box;margin:0;padding:0}
html,body{width:1200px;height:3028px;overflow:hidden}
body{font-family:"Open Sans",Arial,sans-serif;color:var(--text);background:var(--white);position:relative}
h1,h2,h3,h4,.btn,.nav a,.brand{font-family:"Poppins",Arial,sans-serif}
.accent{color:var(--green)}
.btn{display:inline-block;background:var(--green);color:var(--white);font-weight:600;text-decoration:none;border-radius:3px}

/* header */
.site-header{position:absolute;top:0;left:0;width:1200px;height:76px;background:var(--white);display:flex;align-items:center;padding:0 112px;z-index:2}
.brand{display:flex;align-items:center;gap:10px;font-weight:700;font-size:20px;color:var(--ink)}
.brand-mark{width:26px;height:26px;background:var(--green)}
.nav{display:flex;gap:26px;margin-left:120px}
.nav a{font-size:15px;color:var(--ink);text-decoration:none;font-weight:500}
.nav a.active{color:var(--green);border-bottom:2px solid var(--green);padding-bottom:3px}
.header-cta{margin-left:auto;padding:14px 22px;font-size:16px}

/* hero */
.hero{position:absolute;top:76px;left:0;width:1200px;height:524px;background:linear-gradient(180deg,#dfe6ec 0%,#cfd6d6 45%,#a9a196 75%,#8c8172 100%)}
.hero-photo{position:absolute;inset:0;background:radial-gradient(ellipse at 72% 45%,#e3a521 0 11%,rgba(60,60,60,.35) 22%,transparent 40%)}
.hero-content{position:absolute;left:112px;top:150px}
.hero h1{font-size:62px;line-height:1.12;font-weight:700;color:var(--ink)}
.hero .btn{margin-top:38px;padding:15px 30px;font-size:17px}

/* about */
.about{position:absolute;top:600px;left:0;width:1200px;height:460px}
.about-photo{position:absolute;left:112px;top:80px;width:448px;height:300px;background:linear-gradient(135deg,#cfcfcc,#9e9d99);box-shadow:-12px 12px 0 var(--green)}
.about-text{position:absolute;left:640px;top:70px;width:460px}
.about h2{font-size:40px;font-weight:600;color:var(--ink)}
.about p{margin-top:20px;font-size:16px;line-height:1.75}
.about .btn{margin-top:26px;padding:14px 32px;font-size:17px}

/* services */
.services{position:absolute;top:1060px;left:0;width:1200px;height:620px;background:var(--mint)}
.section-title{text-align:center;font-size:42px;font-weight:600;color:var(--ink)}
.services .section-title{margin-top:70px}
.service-list{position:absolute;top:160px;left:112px;display:flex;gap:24px}
.service{width:312px;text-align:center}
.service-photo{height:300px;border-bottom:8px solid var(--green)}
.service h3{margin-top:20px;font-size:24px;font-weight:600;color:var(--ink)}
.arrow{position:absolute;width:24px;height:24px}
.arrow path{fill:none;stroke:var(--ink);stroke-width:3}

/* testimonials */
.testimonials{position:absolute;top:1680px;left:0;width:1200px;height:440px;background:var(--white)}
.testimonials .section-title{margin-top:40px;color:var(--green-dark)}
.quote-card{position:absolute;top:128px;width:480px;height:252px;background:var(--white);box-shadow:0 4px 18px rgba(0,0,0,.13);padding:36px 34px}
.quote-card p{font-size:15px;line-height:1.7}
.reviewer{display:flex;align-items:center;gap:16px;margin-top:22px}
.avatar{width:72px;height:72px;border-radius:50%;background:linear-gradient(135deg,#d9c2a9,#9c7d63)}
.reviewer strong{display:block;font-weight:400;font-size:15px;color:var(--ink)}
.reviewer span{font-size:15px}

/* contact */
.contact{position:absolute;top:2120px;left:0;width:1200px;height:540px;background:var(--mint-2)}
.map{position:absolute;left:0;top:0;width:600px;height:540px;background:linear-gradient(160deg,#e7ece5,#d4e0d0 60%,#c8d8cf)}
.map-pin{position:absolute;left:260px;top:90px;width:60px;height:60px;border-radius:50%;background:var(--white);box-shadow:0 0 0 4px #e24a4a}
.map-label{position:absolute;left:342px;top:94px;font-size:14px;font-weight:600;color:var(--ink);line-height:1.35}
.contact-form{position:absolute;left:640px;top:100px;width:450px}
.contact-form h2{font-size:42px;font-weight:600;color:var(--ink)}
.field{height:54px;margin-top:14px;background:var(--white);border:1px solid var(--line);font-size:15px;color:#999;padding:16px 22px;display:flex;justify-content:space-between}
.contact-form h2+.field{margin-top:22px}
.submit{display:block;margin-top:18px;height:56px;line-height:56px;text-align:center;font-size:18px;border-radius:2px}

/* footer */
.site-footer{position:absolute;top:2660px;left:0;width:1200px;height:368px;border-top:1px solid #eee}
.footer-brand{position:absolute;left:112px;top:46px}
.socials{display:flex;gap:14px;margin-top:26px}
.socials i{display:block;width:30px;height:30px;border-radius:50%;background:var(--green)}
.socials i+i{background:var(--ink)}
.footer-col{position:absolute;top:80px}
.footer-col h4{font-size:18px;font-weight:600;color:var(--green)}
.footer-col ul{list-style:none;margin-top:14px}
.footer-col li{font-size:15px;color:var(--ink);line-height:28px;display:flex;align-items:center;gap:12px}
.footer-col.bullets li::before{content:"";width:7px;height:7px;border-radius:50%;background:var(--green)}
.footer-col .ico{width:28px;height:28px;border-radius:50%;background:var(--green);display:flex;align-items:center;justify-content:center;flex-shrink:0}
.footer-col .ico svg{width:15px;height:15px;fill:var(--white)}
.copyright{position:absolute;left:0;top:322px;width:1200px;text-align:center;font-size:14px;color:var(--ink)}
</style>
</head>
<body>

<header class="site-header">
  <div class="brand"><span class="brand-mark"></span>Brack and Loam</div>
  <nav class="nav">
    <a href="#" class="active">Home</a><a href="#">About</a><a href="#">Services</a><a href="#">Testimonials</a><a href="#">Contact Us</a>
  </nav>
  <a href="#" class="btn header-cta">Get a Free Quote</a>
</header>

<section class="hero">
  <div class="hero-photo" role="img" aria-label="Yellow excavator on a cleared lot with trees behind"></div>
  <div class="hero-content">
    <h1>Land Clearing<br><span class="accent">Pickens County</span></h1>
    <a href="#" class="btn">View Services</a>
  </div>
</section>

<section class="about">
  <div class="about-photo" role="img" aria-label="Stacked paving stones on a work site"></div>
  <div class="about-text">
    <h2>About <span class="accent">Brack and Loam LLC</span></h2>
    <p>Brack and Loam LLC is a locally owned and operated land solutions business proudly serving Pickens County and the surrounding areas of North Georgia. Whether you're preparing a homesite, clearing overgrown acreage, or need reliable hauling equipment, we bring the experience, tools, and local knowledge to get the job done right.</p>
    <a href="#" class="btn">Read More</a>
  </div>
</section>

<section class="services">
  <h2 class="section-title">Our <span class="accent">Services</span></h2>
  <svg class="arrow" style="left:40px;top:340px" viewBox="0 0 24 24"><path d="M15 4 7 12l8 8"/></svg>
  <svg class="arrow" style="left:1132px;top:340px" viewBox="0 0 24 24"><path d="M9 4l8 8-8 8"/></svg>
  <div class="service-list">
    <div class="service"><div class="service-photo" role="img" aria-label="Excavator grading red clay soil" style="background:linear-gradient(160deg,#c9b89a,#a5643b)"></div><h3>Grading</h3></div>
    <div class="service"><div class="service-photo" role="img" aria-label="Worker spreading mulch in a garden bed" style="background:linear-gradient(160deg,#6c9a3c,#5b3b24)"></div><h3>Mulching</h3></div>
    <div class="service"><div class="service-photo" role="img" aria-label="Dump truck on the road" style="background:linear-gradient(160deg,#dfe6ee,#8c949c)"></div><h3>Hauling</h3></div>
  </div>
</section>

<section class="testimonials">
  <h2 class="section-title">Testimonials</h2>
  <svg class="arrow" style="left:40px;top:244px" viewBox="0 0 24 24"><path d="M15 4 7 12l8 8"/></svg>
  <svg class="arrow" style="left:1132px;top:244px" viewBox="0 0 24 24"><path d="M9 4l8 8-8 8"/></svg>
  <div class="quote-card" style="left:100px">
    <p>"Brack and Loam did an incredible job clearing our land in Talking Rock. They showed up on time, worked efficiently, and left the site cleaner than I expected. Highly recommend for anyone needing land cleared in North Georgia."</p>
    <div class="reviewer"><div class="avatar" role="img" aria-label="Customer portrait"></div><div><strong>Dana R.,</strong><span>Talking Rock, GA</span></div></div>
  </div>
  <div class="quote-card" style="left:620px">
    <p>"The grading work they did on our build site was top notch. They took time to explain drainage options and really knew what they were doing. You can tell they take pride in their work."</p>
    <div class="reviewer"><div class="avatar" role="img" aria-label="Customer portrait"></div><div><strong>Mara &amp; Tom K.,</strong><span>Pickens County</span></div></div>
  </div>
</section>

<section class="contact">
  <div class="map" role="img" aria-label="Map of the Pickens County, Georgia service area"></div>
  <div class="map-pin"></div>
  <div class="map-label">Pickens County,<br>Georgia</div>
  <form class="contact-form">
    <h2>Contact <span class="accent">Us</span></h2>
    <div class="field">Name</div>
    <div class="field">Phone Number</div>
    <div class="field">Email Address</div>
    <div class="field">Type of Service <svg width="14" height="14" viewBox="0 0 24 24"><path d="M5 9l7 7 7-7" fill="none" stroke="#444" stroke-width="3"/></svg></div>
    <a href="#" class="btn submit">Submit</a>
  </form>
</section>

<footer class="site-footer">
  <div class="footer-brand">
    <div class="brand"><span class="brand-mark"></span>Brack and Loam</div>
    <div class="socials"><i></i><i></i><i></i><i></i></div>
  </div>
  <div class="footer-col bullets" style="left:380px">
    <h4>Quick Links</h4>
    <ul><li>Home</li><li>About</li><li>Services</li><li>Testimonials</li></ul>
  </div>
  <div class="footer-col bullets" style="left:612px">
    <h4>Our Service Area</h4>
    <ul><li>Jasper, GA</li><li>Talking Rock, GA</li><li>Nelson, GA</li><li>Marble Hill, GA</li><li>Tate, GA</li></ul>
  </div>
  <div class="footer-col" style="left:862px">
    <h4>Contact Us</h4>
    <ul>
      <li><span class="ico"><svg viewBox="0 0 24 24"><path d="M6.6 10.8a15 15 0 0 0 6.6 6.6l2.2-2.2c.3-.3.7-.4 1-.2 1.1.4 2.3.6 3.6.6.6 0 1 .4 1 1V20c0 .6-.4 1-1 1A17 17 0 0 1 3 4c0-.6.4-1 1-1h3.5c.6 0 1 .4 1 1 0 1.3.2 2.5.6 3.6.1.3 0 .7-.2 1z"/></svg></span>555 214 00</li>
      <li><span class="ico"><svg viewBox="0 0 24 24"><path d="M3 5h18v14H3zm2 2v.5l7 4.5 7-4.5V7z"/></svg></span>info@brackandloam.com</li>
      <li style="align-items:flex-start;line-height:22px;margin-top:4px"><span class="ico"><svg viewBox="0 0 24 24"><path d="M12 2a7 7 0 0 0-7 7c0 5 7 13 7 13s7-8 7-13a7 7 0 0 0-7-7zm0 9.5A2.5 2.5 0 1 1 12 6.5a2.5 2.5 0 0 1 0 5z"/></svg></span><span>Brack and Loam LLC<br>Based in: Jasper, GA 30143</span></li>
    </ul>
  </div>
  <p class="copyright">Copyright © 2025 Brack and Loam LLC. All rights reserved.</p>
</footer>

</body>
</html>
```